Business Card Design - Construction Company

Tarrowin Construction is in need of a sharp, modern business card design that has an architectural/high fashion feel.

We are looking for a two sided card.

One side simple dark grey/black with some texture in the background. e.g. (a mosaic of simple interconnecting shapes or a shadow of the logo.) Something to draw attention and create interest.It will need to feature a large Tarrowin construction logo (files attached) in metallic gradient or plain white.

The other side should contain all of our information:

(in largest text)
Name of person
Tarrowin Construction Pty. Ltd.

Licensed builders specialising in:
- Bathrooms
- Kitchens
- Commercial interiors

(mid sized text)
Phone number
Fax number
person@tarrowinconstruction.example.au
www. tarrowinconstruction.example.au

(smaller text)
ABN: 62407938215
BSA license: xxx-xxxx
PO Box 8641 Kellsmoor QLD 4019 (address)

Target Market(s)

professional home and business owners

Industry/Entity Type

Construction

Requirements
Must have
• Must be bold, professional looking and modern.
Nice to have
• We are undecided as to what kind of printing we will go with.
Definitely square edged.
Probably high quality satin card.
We are also interested in designs that would work well on transparent or translucent plastic.
Ideally we would print two versions.
Should not have
• Nothing with an antique feel.
No wild colours. Small amounts of colour can be good in the right place.

```html
<!DOCTYPE html>
<html lang="en">
<head>
<meta charset="utf-8">
<title>Tarrowin Construction – Business Cards</title>
<link rel="stylesheet" href="https://fonts.googleapis.com/css2?family=Michroma&display=swap">
<style>
  :root {
    --stage: #dcdcdc;
    --ink: #111111;
    --steel: #6e6e6e;
    --band: #5c5c5c;
    --panel: #0b0b0b;
    --paper: #ffffff;
    --frost-top: #c9d3d8;
    --frost-mid: #b9a791;
    --frost-low: #c6ced2;
  }
  * { margin: 0; padding: 0; box-sizing: border-box; }
  html, body { width: 1200px; height: 1067px; overflow: hidden; }
  body {
    background: var(--stage);
    font-family: "Michroma", sans-serif;
    position: relative;
  }
  .card {
    position: absolute;
    top: 80px;
    width: 533px;
    height: 931px;
  }
  .card--clear { left: 47px; }
  .card--frosted { left: 620px; }

  .card__frost {
    position: absolute;
    left: 0; top: 0;
    width: 100%; height: 536px;
    background: linear-gradient(180deg, var(--frost-top) 0%, var(--frost-mid) 55%, var(--frost-low) 100%);
    opacity: 0.85;
  }

  .brand {
    position: absolute;
    left: 0; top: 150px;
    width: 100%;
    text-align: center;
  }
  .brand__mark {
    width: 150px; height: 150px;
    margin: 0 auto 46px;
    border-radius: 50%;
    background: var(--steel);
  }
  .brand__name {
    font-size: 30px;
    color: var(--ink);
    letter-spacing: 1px;
  }

  .specialties {
    position: absolute;
    left: 0; top: 536px;
    width: 100%; height: 71px;
    background: var(--band);
    color: var(--paper);
    text-align: center;
    padding-top: 18px;
  }
  .specialties__title { font-size: 19px; letter-spacing: 0.5px; line-height: 22px; }
  .specialties__list { font-size: 13px; letter-spacing: 0.5px; line-height: 22px; }

  .details {
    position: absolute;
    left: 0; top: 607px;
    width: 100%; height: 324px;
    background: var(--panel);
    color: var(--paper);
    text-align: center;
  }
  .details__name {
    position: absolute; left: 0; width: 100%; top: 52px;
    font-size: 25px; font-variant: small-caps; letter-spacing: 0.5px;
  }
  .details__company {
    position: absolute; left: 0; width: 100%; top: 83px;
    font-size: 16px; font-variant: small-caps; letter-spacing: 1px;
  }
  .details__address {
    position: absolute; left: 0; width: 100%; top: 116px;
    font-size: 17px; font-variant: small-caps;
  }
  .contact {
    position: absolute; left: 0; width: 100%; top: 152px;
    list-style: none;
    font-size: 15px; font-variant: small-caps;
    line-height: 21px;
  }
  .contact__item { display: flex; justify-content: center; align-items: center; gap: 6px; }
  .contact__icon { width: 16px; height: 14px; fill: var(--paper); }
  .contact__item--web .contact__icon, .contact__item--mail .contact__icon { fill: none; stroke: var(--paper); stroke-width: 1.4; }
  .registration {
    position: absolute; left: 0; width: 100%; top: 256px;
    font-size: 14px; font-variant: small-caps; line-height: 21px;
  }
</style>
</head>
<body>

  <section class="card card--clear" aria-label="Business card, clear version">
    <div class="brand">
      <div class="brand__mark"></div>
      <div class="brand__name">Tarrowin Construction</div>
    </div>
    <div class="specialties">
      <p class="specialties__title">LICENSED BUILDERS SPECIALISING IN:</p>
      <p class="specialties__list">BATHROOMS &nbsp;|&nbsp; KITCHENS &nbsp;|&nbsp; COMMERCIAL INTERIORS</p>
    </div>
    <div class="details" role="img" aria-label="Black panel with subtle interlocking diamond texture">
      <p class="details__name">Lukas Brenner</p>
      <p class="details__company">Tarrowin Construction Pty. Ltd.</p>
      <p class="details__address">PO Box 8641 Kellsmoor QLD 4019</p>
      <ul class="contact">
        <li class="contact__item"><svg class="contact__icon" viewBox="0 0 16 14"><path d="M1 5c0-3 14-3 14 0v1h-4V4H5v2H1z"/><rect x="3" y="7" width="10" height="6" rx="1"/></svg>000 000 0000</li>
        <li class="contact__item"><svg class="contact__icon" viewBox="0 0 16 14"><rect x="4" y="1" width="8" height="4"/><rect x="1" y="5" width="14" height="6" rx="1"/><rect x="4" y="9" width="8" height="4"/></svg>000 000 0000</li>
        <li class="contact__item contact__item--mail"><svg class="contact__icon" viewBox="0 0 16 14"><rect x="1" y="2" width="14" height="10"/><path d="M1 2l7 6 7-6"/></svg>person@tarrowinconstruction.example.au</li>
        <li class="contact__item contact__item--web"><svg class="contact__icon" viewBox="0 0 16 14"><circle cx="8" cy="7" r="6"/><ellipse cx="8" cy="7" rx="2.5" ry="6"/><path d="M2 7h12"/></svg>www.tarrowinconstruction.example.au</li>
      </ul>
      <p class="registration">ABN: 62407938215<br>BSA license: xxx-xxxx</p>
    </div>
  </section>

  <section class="card card--frosted" aria-label="Business card, frosted textured version">
    <div class="card__frost" role="img" aria-label="Half-clear frosted background with faint diamond texture"></div>
    <div class="brand">
      <div class="brand__mark"></div>
      <div class="brand__name">Tarrowin Construction</div>
    </div>
    <div class="specialties">
      <p class="specialties__title">LICENSED BUILDERS SPECIALISING IN:</p>
      <p class="specialties__list">BATHROOMS &nbsp;|&nbsp; KITCHENS &nbsp;|&nbsp; COMMERCIAL INTERIORS</p>
    </div>
    <div class="details" role="img" aria-label="Black panel with subtle interlocking diamond texture">
      <p class="details__name">Lukas Brenner</p>
      <p class="details__company">Tarrowin Construction Pty. Ltd.</p>
      <p class="details__address">PO Box 8641 Kellsmoor QLD 4019</p>
      <ul class="contact">
        <li class="contact__item"><svg class="contact__icon" viewBox="0 0 16 14"><path d="M1 5c0-3 14-3 14 0v1h-4V4H5v2H1z"/><rect x="3" y="7" width="10" height="6" rx="1"/></svg>000 000 0000</li>
        <li class="contact__item"><svg class="contact__icon" viewBox="0 0 16 14"><rect x="4" y="1" width="8" height="4"/><rect x="1" y="5" width="14" height="6" rx="1"/><rect x="4" y="9" width="8" height="4"/></svg>000 000 0000</li>
        <li class="contact__item contact__item--mail"><svg class="contact__icon" viewBox="0 0 16 14"><rect x="1" y="2" width="14" height="10"/><path d="M1 2l7 6 7-6"/></svg>person@tarrowinconstruction.example.au</li>
        <li class="contact__item contact__item--web"><svg class="contact__icon" viewBox="0 0 16 14"><circle cx="8" cy="7" r="6"/><ellipse cx="8" cy="7" rx="2.5" ry="6"/><path d="M2 7h12"/></svg>www.tarrowinconstruction.example.au</li>
      </ul>
      <p class="registration">ABN: 62407938215<br>BSA license: xxx-xxxx</p>
    </div>
  </section>

</body>
</html>
```